Corvix Thinner Logo and Packaging Design

We are seeking a striking and professional logo and packaging design for our new product line, Corvix Thinner. This logo will be used on the packaging for three different sizes of half-transparent carboys: 1L, 4L, and 20L. Corvix Thinner is a high-quality solvent brand known for its excellent solvency, fast-drying properties, and pleasant smell. The logo should feature an eagle motif to symbolize power and precision, and our slogan, "RISE ABOVE ALL." The design should be suitable for placement on hardware store and warehouse shelves. Additionally, we need the designer to create an eagle logo to accompany the packaging.

Packaging Dimensions:
1L Carboy:
Front: 71mm height x 142mm width
Side: 71mm height x 73mm width
4L Carboy:
Front: 160mm height x 170mm width
Side: 160mm height x 120mm width
20L Carboy:
Front: 245mm height x 190mm width
Side: 215mm height x 190mm width
Front Label Requirements:

Product Name: Thinner QZR
Volume: 20L
Precautionary Statements:
Keep Away from Sources of ignition - No Smoking
Avoid Contact with Eyes
Do Not Empty into Drains or Sewers
Take Precautionary Measures Against Static Discharge
Hazard Statements:
Flammable Liquid and Vapor
May be fatal if swallowed or enters Airways
Causes Skin Irritation
Causes Serious Eye Irritation
Causes Damage to Organs if Prolonged or Repeated Exposure
Hazard Pictograms: (Include relevant hazard symbols)
Design Requirements:

Logo: Eagle motif (to be designed by the designer)
Slogan: RISE ABOVE ALL
Color Scheme: Designer to recommend (should be striking and professional for retail display)

Please see my latest picture. Kindly note the packaging is in Plastic Carboy (not in metal tin as per PS).

Eagle to be more majestic and bigger (as if soaring in the sky).
Singapore landscape as background to have Singapore identity such as KDT, Lumen Loop, terraces of mistral etc.

Eagle to be more majestic and bigger, wings to spread wide.
We not want it to be of photo style, but more on a cartoon style. Please see my latest file uploaded.

Target Market(s)

Our target market includes painting companies, construction companies, direct household consumers, and industrial users who require high-quality solvents for various applications.

Industry/Entity Type

Chemical, spray paint and painting, household, industrial

Requirements
Must have
• Professional and Striking Design: Eye-catching and professional packaging for retail shelves. Eagle Logo: A strong, precise eagle logo. Slogan: "RISE ABOVE ALL" prominently displayed. Clear Precautionary and Hazard Statements: Important safety information and pictograms. Volume Indication: Clearly marked (e.g., 1L, 4L, 20L). Eagle to be more majestic and bigger (as if soaring in the sky). Singapore landscape as background to have Singapore identity such as KDT, Lumen Loop, terraces of mistral etc.
Nice to have
• Color Scheme Recommendations: Suggestions for a professional, striking color scheme. Versatility: Design elements adaptable across different sizes of packaging. Environmentally Friendly Elements: Indications of sustainability or eco-friendliness in the design.
Should not have
• Overly Complex Designs: Avoid cluttered or overly intricate designs that detract from readability. Inconsistent Branding: Ensure all elements are cohesive and align with the brand identity.

```html
<!DOCTYPE html>
<html lang="en">
<head>
<meta charset="utf-8">
<title>Corvix Thinner QZR – Front Label</title>
<link rel="stylesheet" href="https://fonts.googleapis.com/css2?family=Montserrat:wght@400;500;900&display=swap">
<style>
  :root {
    --label-yellow: #e8dd2a;
    --label-black: #231f20;
    --slogan-grey: #6a6b6d;
    --address-grey: #a3a3a3;
    --text-white: #ffffff;
    --page-bg: #f4f4f4;
    --hazard-red: #e0202a;
  }
  * { box-sizing: border-box; margin: 0; padding: 0; }
  html, body {
    width: 996px; height: 1200px; overflow: hidden;
    background: var(--page-bg);
    font-family: "Montserrat", Arial, sans-serif;
  }
  .canvas { position: relative; width: 996px; height: 1200px; }
  .label {
    position: absolute; left: 30px; top: 163px;
    width: 936px; height: 873px;
  }
  .label-top {
    position: absolute; left: 0; top: 0; width: 936px; height: 450px;
    background: var(--label-yellow);
  }
  .label-bottom {
    position: absolute; left: 0; top: 450px; width: 936px; height: 423px;
    background: var(--label-black);
  }
  .volume { position: absolute; left: 86px; top: 22px; color: var(--text-white); font-weight: 900; }
  .volume-number { display: block; font-size: 150px; line-height: 1; letter-spacing: -10px; }
  .volume-unit { display: block; font-size: 45px; line-height: 1; letter-spacing: -2px; margin-top: -4px; }
  .brand-name {
    position: absolute; left: 82px; top: 232px;
    color: var(--label-black); font-weight: 900;
    font-size: 118px; line-height: 100px; letter-spacing: -5px;
  }
  .brand-name span { display: block; }
  .brand-mark {
    position: absolute; left: 640px; top: 150px;
    width: 110px; height: 110px; border-radius: 50%;
    background: var(--label-black);
  }
  .grade {
    position: absolute; left: 84px; top: 10px;
    color: var(--label-yellow); font-weight: 900; font-size: 92px; line-height: 1; letter-spacing: 2px;
  }
  .safety { position: absolute; left: 86px; color: var(--text-white); }
  .safety h2 { font-weight: 400; font-size: 20px; line-height: 22px; }
  .safety ol { list-style: none; font-size: 13px; font-weight: 500; line-height: 16px; }
  .safety li { padding-left: 16px; text-indent: -16px; }
  .precautions { top: 100px; }
  .hazards { top: 193px; }
  .pictograms { position: absolute; left: 96px; top: 328px; display: flex; gap: 6px; }
  .pictograms svg { width: 74px; height: 74px; }
  .slogan {
    position: absolute; right: 58px; top: 16px; text-align: right;
    color: var(--slogan-grey); font-weight: 900; font-size: 92px; line-height: 80px; letter-spacing: -3px;
  }
  .company {
    position: absolute; right: 62px; top: 334px; text-align: right;
    color: var(--address-grey); font-size: 15px; line-height: 18px; font-style: normal;
  }
</style>
</head>
<body>
<main class="canvas">
  <section class="label">
    <div class="label-top">
      <p class="volume"><span class="volume-number">18</span><span class="volume-unit">LITERS</span></p>
      <h1 class="brand-name"><span>CORVIX</span><span>THINNER</span></h1>
      <div class="brand-mark" aria-hidden="true"></div>
    </div>
    <div class="label-bottom">
      <p class="grade">QZR</p>
      <div class="safety precautions">
        <h2>Precautionary</h2>
        <ol>
          <li>1.&nbsp; Keep Away from Sources of ignition - No Smoking</li>
          <li>2.&nbsp; Avoid Contact with Eyes</li>
          <li>3.&nbsp; Do Not Empty into Drains or Sewers</li>
          <li>4.&nbsp; Take Precautionary Measures Against Static Discharge</li>
        </ol>
      </div>
      <div class="safety hazards">
        <h2>Hazards</h2>
        <ol>
          <li>1.&nbsp; Flammable Liquid and Vapor</li>
          <li>2.&nbsp; May be fatal if swallowed or enters Airways</li>
          <li>3.&nbsp; Causes Skin Irritation</li>
          <li>4.&nbsp; Causes Serious Eye Irritation</li>
          <li>5.&nbsp; Causes Damage to Organs if Prolonged<br>&nbsp;&nbsp;&nbsp;&nbsp; or Repeated Exposure</li>
        </ol>
      </div>
      <div class="pictograms">
        <svg viewBox="0 0 100 100" role="img" aria-label="Flammable hazard pictogram">
          <polygon points="50,4 96,50 50,96 4,50" fill="#fff" stroke="var(--hazard-red)" stroke-width="7"/>
          <path d="M50 28 C60 40 64 48 60 60 C58 66 42 66 40 60 C37 52 42 46 46 40 C46 48 50 50 52 46 C54 40 50 34 50 28 Z" fill="#000"/>
          <rect x="36" y="66" width="28" height="5" fill="#000"/>
        </svg>
        <svg viewBox="0 0 100 100" role="img" aria-label="Health hazard pictogram">
          <polygon points="50,4 96,50 50,96 4,50" fill="#fff" stroke="var(--hazard-red)" stroke-width="7"/>
          <circle cx="50" cy="50" r="16" fill="#000"/>
        </svg>
        <svg viewBox="0 0 100 100" role="img" aria-label="Irritant warning pictogram">
          <polygon points="50,4 96,50 50,96 4,50" fill="#fff" stroke="var(--hazard-red)" stroke-width="7"/>
          <rect x="45" y="26" width="10" height="32" rx="3" fill="#000"/>
          <circle cx="50" cy="68" r="6" fill="#000"/>
        </svg>
      </div>
      <p class="slogan">RISE<br>ABOVE<br>ALL</p>
      <address class="company">Veltrane Pte Ltd<br>48 Harlow Rd #05-11B<br>Meridian 502317</address>
    </div>
  </section>
</main>
</body>
</html>
```